Chat Software Business Card Design

We need a business card design for our company.

We provide businesses with a platform to communicate with their web visitors in real time using chat boxes on their web sites.

We're using a bright color scheme to attract attention on the site and the business card would do well to reflect this also to maintain brand awareness. However it is not essential to the ultimate design to use the same color scheme or feel as the site.

We offer a Free Trial of the software and would encourage a business card design to promote this if possible.

http://qz7mockups3.co.uk/drafts/lumen/index2.html

You will find the company logo attached also.

An eye catching design with something that will set the card apart from others is required.

The design of the card/theme of the card should be very unique, setting our selves apart, eye catching whilst not providing a "wacky" image for the company.

It should also include our contact information;~
Website - www.harbel-talk.com
Email - support@harbel-talk.com
Twitter - @Harbeltalk

Industry/Entity Type

Software

Contact Information for Business Card

Web - www.harbel-talk.com
Email - office@harbel-talk.com
Skype - Harbel.Talk

Requirements
Must have
• Use of company logo is required.

```html
<!DOCTYPE html>
<html lang="en">
<head>
<meta charset="utf-8">
<title>Harbel Talk Business Card</title>
<link rel="stylesheet" href="https://fonts.googleapis.com/css2?family=Open+Sans:wght@400;600;700;800&display=swap">
<style>
  :root {
    --bg: #b9c3c3;
    --card: #0c0c0c;
    --orange: #f0501e;
    --amber: #f6a234;
    --white: #ffffff;
    --muted: #d9d9d9;
  }
  * { margin: 0; padding: 0; box-sizing: border-box; }
  html, body { width: 1200px; height: 896px; overflow: hidden; }
  body {
    background: var(--bg);
    font-family: "Open Sans", Arial, sans-serif;
    display: flex;
    align-items: center;
    justify-content: center;
    gap: 40px;
  }
  .card {
    position: relative;
    width: 540px;
    height: 310px;
    background: var(--orange);
    overflow: hidden;
    box-shadow: 0 10px 24px rgba(0,0,0,.25);
  }
  .card__body { position: absolute; inset: 0; width: 100%; height: 100%; }
  .card__body .sheet { fill: var(--card); }

  .brand {
    position: absolute;
    display: flex;
    align-items: center;
    gap: 10px;
    color: var(--orange);
    font-weight: 800;
    letter-spacing: -0.5px;
  }
  .brand__mark { width: 18px; height: 18px; background: var(--amber); }

  .front .brand { left: 44px; top: 56px; font-size: 44px; }
  .tab { position: absolute; background: var(--amber); }
  .front .tab { left: 0; top: 132px; width: 26px; height: 36px; }
  .person { position: absolute; left: 44px; top: 132px; }
  .person__name {
    color: var(--white);
    font-weight: 700;
    font-size: 22px;
    letter-spacing: 1.5px;
    line-height: 1.1;
  }
  .person__role {
    color: var(--orange);
    font-size: 11px;
    letter-spacing: 5.2px;
    margin-top: 2px;
  }
  .contacts {
    position: absolute;
    right: 30px;
    bottom: 26px;
    list-style: none;
    color: var(--white);
    font-size: 11.5px;
    font-weight: 600;
    line-height: 1.25;
  }
  .contacts li { display: flex; align-items: center; gap: 10px; margin-top: 6px; }
  .contacts svg { width: 14px; height: 14px; flex: none; fill: var(--orange); }

  .back .brand { left: 0; right: 0; justify-content: center; top: 92px; font-size: 48px; }
  .back .tab { right: 0; top: 206px; width: 18px; height: 32px; }
  .socials {
    position: absolute;
    left: 40px;
    right: 40px;
    top: 210px;
    display: flex;
    justify-content: space-between;
    list-style: none;
    color: var(--muted);
    font-size: 11px;
  }
  .socials li { display: flex; align-items: center; gap: 10px; }
  .socials .dot { width: 16px; height: 16px; background: var(--amber); }
</style>
</head>
<body>

  <section class="card front" aria-label="Business card front">
    <svg class="card__body" viewBox="0 0 540 310" preserveAspectRatio="none" aria-hidden="true">
      <path class="sheet" d="M0,8 C180,10 380,22 540,54 L540,310 L0,310 Z"/>
    </svg>
    <div class="brand"><span class="brand__mark"></span>Harbel Talk</div>
    <div class="tab"></div>
    <div class="person">
      <p class="person__name">DARIO WENSLEY</p>
      <p class="person__role">GENERAL MANAGER</p>
    </div>
    <ul class="contacts">
      <li>
        <svg viewBox="0 0 16 16"><path d="M8 1 1 7.5h2V15h4v-4h2v4h4V7.5h2z"/></svg>
        <span>27 4th floor Plaza<br>Keller Road MNB</span>
      </li>
      <li>
        <svg viewBox="0 0 16 16"><path d="M8 1a7 7 0 1 0 0 14A7 7 0 0 0 8 1zm0 1.5c.9 0 1.9 1.6 2.2 4.5H5.8C6.1 4.1 7.1 2.5 8 2.5zM2.6 7h1.9c0-1.5.4-3 .9-4A5.5 5.5 0 0 0 2.6 7zm0 2a5.5 5.5 0 0 0 2.8 4c-.5-1-.9-2.5-.9-4zm3.2 0h4.4c-.3 2.9-1.3 4.5-2.2 4.5S6.1 11.9 5.8 9zm5.7 0c0 1.5-.4 3-.9 4a5.5 5.5 0 0 0 2.8-4zm1.9-2a5.5 5.5 0 0 0-2.8-4c.5 1 .9 2.5.9 4z"/></svg>
        <span>www.harbel-talk.com</span>
      </li>
      <li>
        <svg viewBox="0 0 16 16"><path d="M1 3h14v10H1zm1.5 1.5v.4L8 9l5.5-4.1v-.4zm0 2.2v4.8h11V6.7L8 10.8z"/></svg>
        <span>office@harbel-talk.com</span>
      </li>
      <li>
        <svg viewBox="0 0 16 16"><path d="M4 1.5 6.5 4 5 6c.8 1.8 2.2 3.2 4 4l2-1.5 2.5 2.5-1.5 2.5C7 13 3 9 2 3.5z"/></svg>
        <span>014 552 7180</span>
      </li>
    </ul>
  </section>

  <section class="card back" aria-label="Business card back">
    <svg class="card__body" viewBox="0 0 540 310" preserveAspectRatio="none" aria-hidden="true">
      <path class="sheet" d="M0,0 L400,0 C460,20 510,50 540,78 L540,310 L0,310 Z"/>
    </svg>
    <div class="brand"><span class="brand__mark"></span>Harbel Talk</div>
    <ul class="socials">
      <li><span class="dot"></span>yourname</li>
      <li><span class="dot"></span>@yourname</li>
      <li><span class="dot"></span>yourname</li>
    </ul>
    <div class="tab"></div>
  </section>

</body>
</html>
```